Business Card Design Project

Design a business card for a new entity that is in the OTC (over-the-counter-derivative brokering business-Financial Services.
The card should be clean a professional looking. We encourage designers to think pro-actively, fresh and innovative, but also keep in mind that only 2 things are important. a)that the card look professional b)that it is somehow memorable.

We have a new logo which we will upload and will want the Trident symbol in the logo to be raised OR not have the symbol raised and plan on having the word " BROKERAGE SERVICES" raised that stands out and will look sharp.

Along with uploading the new logo which MUST be incorperated, I am also going to upload 3 different business cards of other businesses to use only as guild-lines since I think they are clean and professional looking BUT I encourage all to be pro-active and creative on their own.

Industry/Entity Type

Business

Requirements
Must have
• 1. MUST HAVE THE NEW LOGO WHICH WILL BE UPLOADED
2. MUST HAVE A VERSION SIMILAR TO THE 3 DIFFERENT BUSINESS CARDS I WILL UPLOAD, BUT EACH DESIGNER MUST ONLY THESE THIS FORMAT AS A BACK-UP AND BE CREATIVE ON THEIR OWN FIRST. ALSO WHEN LOOKING AT THE CARDS WHICH I UPLOAD TO USE AS A GUILD-LINE KEEP IN MIND THAT THESE ARE KESTRAVEL 300 COMPANIES SO DO NOT MIMIC ONLY USE FOR IDEAS.
Nice to have
• these are the 3 different other biz cards to look at for some reference

```html
<!DOCTYPE html>
<html lang="en">
<head>
<meta charset="utf-8">
<title>Halcyon Brokerage Services – Business Cards</title>
<link rel="stylesheet" href="https://fonts.googleapis.com/css2?family=Source+Sans+3:wght@400;600&display=swap">
<style>
  :root {
    --page: #ffffff;
    --card-dark: #2b2c2e;
    --card-dark-2: #38393b;
    --card-light: #ffffff;
    --ink: #3a3c3f;
    --ink-soft: #55585b;
    --gold: #d4a819;
    --gold-light: #f2d35a;
    --gold-deep: #c49a10;
    --steel: #1d1e20;
    --steel-light: #5b6062;
    --rule: #c9cbcd;
    --white: #ffffff;
  }
  * { box-sizing: border-box; margin: 0; padding: 0; }
  html, body {
    width: 1200px; height: 900px; overflow: hidden;
    background: var(--page);
    font-family: "Source Sans 3", "Myriad Pro", Arial, sans-serif;
  }
  .sheet { position: relative; width: 1200px; height: 900px; }
  .icons { position: absolute; width: 0; height: 0; }

  .card {
    position: absolute; width: 493px; height: 282px;
    background: var(--card-light);
    box-shadow: 5px 6px 6px rgba(0,0,0,0.35);
    overflow: hidden;
  }
  .card--front { left: 79px; top: 158px; background: linear-gradient(180deg, var(--card-dark-2), var(--card-dark)); }
  .card--a { left: 643px; top: 158px; }
  .card--b { left: 79px;  top: 491px; }
  .card--c { left: 643px; top: 491px; }

  /* name mark */
  .mark { position: absolute; text-align: center; color: var(--ink); font-weight: 400; }
  .mark__dot { display: block; margin: 0 auto 14px; width: 54px; height: 54px; border-radius: 50%; background: var(--gold); }
  .mark__name { display: block; font-size: 44px; letter-spacing: 2px; line-height: 1; }
  .mark__sub { display: block; font-size: 12.5px; letter-spacing: 3.6px; margin-top: 6px; line-height: 1; }

  .card--front .mark { left: 0; width: 100%; top: 52px; color: var(--white); }
  .card--front .mark__dot { width: 62px; height: 62px; margin-bottom: 14px; }
  .sites { position: absolute; left: 0; width: 100%; top: 218px; text-align: center; color: var(--white); font-size: 13.5px; line-height: 16.5px; }

  .card--a .mark, .card--b .mark, .card--c .mark { left: 30px; width: 205px; top: 62px; }

  .divider { position: absolute; left: 246px; top: 54px; width: 2px; height: 168px;
    background: linear-gradient(180deg, rgba(201,203,205,0), var(--rule) 30%, var(--rule) 70%, rgba(201,203,205,0)); }

  .details { position: absolute; left: 267px; top: 52px; color: var(--ink); font-size: 13px; line-height: 16.3px; }
  .details__name { color: var(--gold); font-size: 20px; font-weight: 600; line-height: 24px; }
  .details__role { color: var(--ink-soft); margin-bottom: 12px; }
  .details__row { display: flex; align-items: center; gap: 5px; }
  .details__row svg { width: 12px; height: 12px; fill: var(--gold); flex: none; }

  .memberships { position: absolute; left: 0; width: 100%; top: 246px; text-align: center; font-size: 10px; color: var(--ink); }
  .memberships .sep { color: var(--gold); padding: 0 2px; }

  .band { position: absolute; left: 0; bottom: 0; width: 100%; height: 15px; }
  .band--steel { background: linear-gradient(90deg, var(--steel) 0%, var(--steel-light) 62%, var(--steel) 100%); }
  .band--split { background:
      linear-gradient(90deg, var(--gold-deep) 0%, var(--gold-light) 55%, var(--gold-deep) 100%) 17px 0 / 228px 100% no-repeat,
      linear-gradient(90deg, var(--steel) 0%, var(--steel) 45%, var(--steel-light) 75%, var(--steel) 100%); }
  .band--gold { background: linear-gradient(90deg, var(--gold-deep) 0%, var(--gold) 35%, var(--gold-light) 65%, var(--gold) 100%); }
</style>
</head>
<body>
<svg class="icons" aria-hidden="true">
  <defs>
    <symbol id="i-phone" viewBox="0 0 12 12"><path d="M2.6 1l2 2.3-1 1.2c.7 1.5 1.8 2.6 3.3 3.3l1.2-1L10.4 9 9.3 11C5 10.5 1.5 7 1 2.7z"/></symbol>
    <symbol id="i-mobile" viewBox="0 0 12 12"><path d="M3.5 0.5h5v11h-5zM4.5 1.7v7.6h3V1.7z"/></symbol>
    <symbol id="i-mail" viewBox="0 0 12 12"><path d="M1 3h10v6.5H1zM1.6 3.4L6 6.6l4.4-3.2z"/></symbol>
    <symbol id="i-chat" viewBox="0 0 12 12"><path d="M6 .5a5.5 5.5 0 1 1 0 11 5.5 5.5 0 0 1 0-11zM6 3a1.6 1.6 0 1 0 0 3.2A1.6 1.6 0 0 0 6 3zM3.3 9h5.4C8.3 7.6 7.3 7 6 7S3.7 7.6 3.3 9z"/></symbol>
    <symbol id="i-web" viewBox="0 0 12 12"><path d="M6 .5a5.5 5.5 0 1 1 0 11 5.5 5.5 0 0 1 0-11zM2 5.4h2.3c.1-1.4.4-2.6.9-3.5A4.3 4.3 0 0 0 2 5.4zm3.3 0h1.4C6.6 4 6.4 2.8 6 2c-.4.8-.6 2-.7 3.4zm2.4 0H10a4.3 4.3 0 0 0-3.2-3.5c.5.9.8 2.1.9 3.5zM2 6.6a4.3 4.3 0 0 0 3.2 3.5c-.5-.9-.8-2.1-.9-3.5zm3.3 0c.1 1.4.3 2.6.7 3.4.4-.8.6-2 .7-3.4zm2.4 0c-.1 1.4-.4 2.6-.9 3.5A4.3 4.3 0 0 0 10 6.6z"/></symbol>
  </defs>
</svg>

<main class="sheet">
  <section class="card card--front">
    <div class="mark">
      <span class="mark__dot"></span>
      <span class="mark__name">HALCYON</span>
      <span class="mark__sub">BROKERAGE SERVICES</span>
    </div>
    <div class="sites">
      <div>www.HalcyonBrokerageServices.com</div>
      <div>www.HalcyonFutures.com</div>
      <div>www.HalcyonOTC.com</div>
    </div>
  </section>

  <section class="card card--a">
    <div class="mark"><span class="mark__dot"></span><span class="mark__name">HALCYON</span><span class="mark__sub">BROKERAGE SERVICES</span></div>
    <div class="divider"></div>
    <div class="details">
      <div class="details__name">Daniel Reyes</div>
      <div class="details__role">Principal Consultant</div>
      <div>1876 Marlow Court #204</div>
      <div>Tampa, FL 33602</div>
      <div class="details__row"><svg><use href="#i-phone"/></svg>+1 (000) 000 - 0000</div>
      <div class="details__row"><svg><use href="#i-mobile"/></svg>+1 (000) 000 - 0000</div>
      <div class="details__row"><svg><use href="#i-mail"/></svg>dreyes@halcyonbrokerage.com</div>
      <div class="details__row"><svg><use href="#i-chat"/></svg>dreyes@chatline.com</div>
      <div class="details__row"><svg><use href="#i-web"/></svg>www.halcyonbrokerage.com</div>
    </div>
    <div class="memberships">Members of Norden Exchange <span class="sep">•</span> Members of Vantor ClearNet <span class="sep">•</span> Members of Guild of Independent Day Traders</div>
    <div class="band band--steel"></div>
  </section>

  <section class="card card--b">
    <div class="mark"><span class="mark__dot"></span><span class="mark__name">HALCYON</span><span class="mark__sub">BROKERAGE SERVICES</span></div>
    <div class="divider"></div>
    <div class="details">
      <div class="details__name">Daniel Reyes</div>
      <div class="details__role">Principal Consultant</div>
      <div>1876 Marlow Court #204</div>
      <div>Tampa, FL 33602</div>
      <div class="details__row"><svg><use href="#i-phone"/></svg>+1 (000) 000 - 0000</div>
      <div class="details__row"><svg><use href="#i-mobile"/></svg>+1 (000) 000 - 0000</div>
      <div class="details__row"><svg><use href="#i-mail"/></svg>dreyes@halcyonbrokerage.com</div>
      <div class="details__row"><svg><use href="#i-chat"/></svg>dreyes@chatline.com</div>
      <div class="details__row"><svg><use href="#i-web"/></svg>www.halcyonbrokerage.com</div>
    </div>
    <div class="memberships">Members of Norden Exchange <span class="sep">•</span> Members of Vantor ClearNet <span class="sep">•</span> Members of Guild of Independent Day Traders</div>
    <div class="band band--split"></div>
  </section>

  <section class="card card--c">
    <div class="mark"><span class="mark__dot"></span><span class="mark__name">HALCYON</span><span class="mark__sub">BROKERAGE SERVICES</span></div>
    <div class="divider"></div>
    <div class="details">
      <div class="details__name">Daniel Reyes</div>
      <div class="details__role">Principal Consultant</div>
      <div>1876 Marlow Court #204</div>
      <div>Tampa, FL 33602</div>
      <div class="details__row"><svg><use href="#i-phone"/></svg>+1 (000) 000 - 0000</div>
      <div class="details__row"><svg><use href="#i-mobile"/></svg>+1 (000) 000 - 0000</div>
      <div class="details__row"><svg><use href="#i-mail"/></svg>dreyes@halcyonbrokerage.com</div>
      <div class="details__row"><svg><use href="#i-chat"/></svg>dreyes@chatline.com</div>
      <div class="details__row"><svg><use href="#i-web"/></svg>www.halcyonbrokerage.com</div>
    </div>
    <div class="memberships">Members of Norden Exchange <span class="sep">•</span> Members of Vantor ClearNet <span class="sep">•</span> Members of Guild of Independent Day Traders</div>
    <div class="band band--gold"></div>
  </section>
</main>
</body>
</html>
```